TQ Regulatory Partners - Biz Card - Re-do

I would like a re-do on my business card.

See my Internet site - tqregpartners.com

1) Remove direct phone line.
2) Add company moto - integrity, diligence, and excellence
3) Add Consulting Services listing:
-Benefit Technology
-ERISA Compliance
-Contract/Vendor Management
-Human Resource/Payroll
-Medical/Prescription Drug
-Integrated Leave of Absence

Target Market(s)

Employee benefit consulting and insurance purchasers, Usually human resource executives

Industry/Entity Type

Human Resource

Contact Information for Business Card

Same business card color scheme, logo,

Font styles to use
Sans Serif

Requirements
Must have
• Same color scheme and logo. Remove direct phone number. Keep all numbers, internet address.

```html
<!DOCTYPE html>
<html lang="en">
<head>
<meta charset="utf-8">
<title>TQ Regulatory Partners – Business Card</title>
<link rel="stylesheet" href="https://fonts.googleapis.com/css2?family=Roboto:wght@300;400;500&display=swap">
<style>
  :root {
    --backdrop: #1c1c1e;
    --plum: #6b2150;
    --plum-deep: #611c48;
    --slate-light: #7f8186;
    --slate-dark: #66686d;
    --white: #ffffff;
    --white-soft: rgba(255,255,255,0.82);
    --icon-grey: #8c8d92;
    --rule: rgba(255,255,255,0.55);
  }
  html, body {
    margin: 0;
    padding: 0;
    width: 1200px;
    height: 1200px;
    overflow: hidden;
    background: var(--backdrop);
  }
  .canvas {
    position: relative;
    width: 1200px;
    height: 1200px;
    font-family: "Roboto", sans-serif;
  }
  .card {
    position: absolute;
    left: 170px;
    width: 860px;
    height: 490px;
    box-shadow: 0 10px 30px rgba(0,0,0,0.55);
  }

  /* Front side */
  .card-front {
    top: 90px;
    background: linear-gradient(135deg, var(--slate-dark), var(--slate-light));
    text-align: center;
  }
  .brand-dot {
    position: absolute;
    left: 50%;
    top: 120px;
    width: 110px;
    height: 110px;
    margin-left: -55px;
    border-radius: 50%;
    background: var(--plum);
  }
  .brand-name {
    position: absolute;
    left: 0;
    right: 0;
    top: 252px;
    margin: 0;
    font-weight: 400;
    font-size: 42px;
    color: var(--white);
    letter-spacing: 0.5px;
  }
  .motto {
    position: absolute;
    left: 0;
    right: 0;
    top: 360px;
    margin: 0;
    font-size: 17px;
    letter-spacing: 1px;
    color: var(--white);
  }
  .motto .sep {
    display: inline-block;
    width: 6px;
    height: 6px;
    border-radius: 50%;
    background: var(--white);
    margin: 0 14px;
    vertical-align: middle;
  }

  /* Back side */
  .card-back {
    top: 620px;
    background: linear-gradient(135deg, var(--plum-deep), var(--plum));
    color: var(--white);
  }
  .holder {
    position: absolute;
    left: 62px;
    top: 40px;
  }
  .holder-name {
    margin: 0;
    font-size: 32px;
    font-weight: 400;
    line-height: 1.1;
  }
  .holder-title {
    margin: 2px 0 0;
    font-size: 19px;
    font-weight: 300;
  }
  .services {
    position: absolute;
    left: 62px;
    top: 132px;
    width: 540px;
  }
  .services-heading {
    margin: 0 0 8px;
    font-size: 14px;
    font-weight: 500;
    letter-spacing: 2px;
    text-transform: uppercase;
    color: var(--white-soft);
  }
  .services-list {
    margin: 0;
    padding: 0;
    list-style: none;
    display: grid;
    grid-template-columns: 1fr 1fr;
    column-gap: 24px;
    row-gap: 6px;
    font-size: 16px;
    font-weight: 300;
  }
  .services-list li::before {
    content: "";
    display: inline-block;
    width: 5px;
    height: 5px;
    border-radius: 50%;
    background: var(--white);
    margin-right: 10px;
    vertical-align: middle;
  }
  .brand-badge {
    position: absolute;
    right: 70px;
    top: 110px;
    width: 170px;
    height: 170px;
    border-radius: 50%;
    background: var(--white);
    display: flex;
    align-items: center;
    justify-content: center;
    text-align: center;
    color: var(--plum);
    font-size: 19px;
    font-weight: 400;
    line-height: 1.25;
  }
  .divider {
    position: absolute;
    left: 45px;
    right: 45px;
    top: 305px;
    height: 1px;
    background: var(--rule);
  }
  .contact-list {
    position: absolute;
    left: 40px;
    top: 326px;
    margin: 0;
    padding: 0;
    list-style: none;
    font-size: 21px;
    font-weight: 300;
    line-height: 34px;
  }
  .contact-list li {
    display: flex;
    align-items: center;
  }
  .contact-list svg {
    width: 22px;
    height: 22px;
    margin-right: 18px;
    fill: var(--icon-grey);
  }
  .address {
    position: absolute;
    right: 70px;
    top: 330px;
    margin: 0;
    text-align: right;
    font-size: 21px;
    font-weight: 300;
    line-height: 34px;
    font-style: normal;
  }
</style>
</head>
<body>
<main class="canvas">

  <section class="card card-front" aria-label="Card front">
    <span class="brand-dot"></span>
    <h1 class="brand-name">TQ Regulatory Partners</h1>
    <p class="motto">Integrity<span class="sep"></span>Diligence<span class="sep"></span>and Excellence</p>
  </section>

  <section class="card card-back" aria-label="Card back">
    <div class="holder">
      <h2 class="holder-name">Daniel Whitmore</h2>
      <p class="holder-title">President</p>
    </div>

    <div class="services">
      <h3 class="services-heading">Consulting Services</h3>
      <ul class="services-list">
        <li>Benefit Technology</li>
        <li>Human Resource/Payroll</li>
        <li>ERISA Compliance</li>
        <li>Medical/Prescription Drug</li>
        <li>Contract/Vendor Management</li>
        <li>Integrated Leave of Absence</li>
      </ul>
    </div>

    <div class="brand-badge">TQ Regulatory<br>Partners</div>

    <div class="divider"></div>

    <ul class="contact-list">
      <li>
        <svg viewBox="0 0 24 24" aria-hidden="true"><path d="M7 3h10v4H7zM4 8h16a2 2 0 0 1 2 2v6h-4v4H6v-4H2v-6a2 2 0 0 1 2-2zm4 7v3h8v-3z"/></svg>
        555.201.7341
      </li>
      <li>
        <svg viewBox="0 0 24 24" aria-hidden="true"><path d="M2 5h20v14H2zm2 2v.5l8 5 8-5V7zm0 2.8V17h16V9.8l-8 5z"/></svg>
        dwhitmore@tqregpartners.com
      </li>
      <li>
        <svg viewBox="0 0 24 24" aria-hidden="true"><path d="M12 2a10 10 0 1 0 0 20 10 10 0 0 0 0-20zm6.9 9h-3a15 15 0 0 0-1.3-6 8 8 0 0 1 4.3 6zM12 4.1c.9 1.3 1.7 3.7 1.9 6.9h-3.8c.2-3.2 1-5.6 1.9-6.9zM9.4 5a15 15 0 0 0-1.3 6h-3A8 8 0 0 1 9.4 5zM5.1 13h3a15 15 0 0 0 1.3 6 8 8 0 0 1-4.3-6zm6.9 6.9c-.9-1.3-1.7-3.7-1.9-6.9h3.8c-.2 3.2-1 5.6-1.9 6.9zm2.6-.9a15 15 0 0 0 1.3-6h3a8 8 0 0 1-4.3 6z"/></svg>
        tqregpartners.com
      </li>
    </ul>

    <address class="address">
      180 Harbor Street NE, Suite 300<br>
      Lakeview, MI 49010
    </address>
  </section>

</main>
</body>
</html>
```